ReDesign Website for a more Bold approach

Hello! I'd like to redesign my website: holvencrest.com

I'd like to add one thing that's not on my website which is a blog. The design around the blog should be put time into as I will be putting out incredibly great content and want it to attract viewers.

I get a lot of inspiration from ruvtal.com (the way they flow the big statements across each screen, colors)
moorlane.vc (the simplicity behind the design is beautiful)

I like modern very simple but bold approaches.

I am going to attach my logo here and if it can be thought of when making the design of the website. Thanks!

Industry/Entity Type

Finance and Private Equity

Number of Pages Required

3 page

Font styles to use
Serif
Sans Serif

Colors
0054AA
0677BA
7BADD7
CADEEF
E8F1F8
0094D4
00A9DD
6FCCEA
C7EBF8
E9F6FB
00AB8E
00BBA5
67D7C9
C6EFE9
E9F9F6

Requirements
Must have
• My project must have a Home, Expertise, Story, Clients, Approach, Blog, Contact
Nice to have
• It would be nice to have these tabs reduced to 1-3 pages
Should not have
• My project must not have bright colors.

```html
<!DOCTYPE html>
<html lang="en">
<head>
<meta charset="utf-8">
<title>Holvencrest Ventures — Finance and Private Equity</title>
<link href="https://fonts.googleapis.com/css2?family=Josefin+Sans:wght@600;700&family=Poppins:wght@400;500;600&display=swap" rel="stylesheet">
<style>
:root{
  --navy:#0c2b4b;
  --accent:#0054aa;
  --accent-mid:#0677ba;
  --accent-soft:#7badd7;
  --hero-bg:#e8f1f8;
  --story-bg:#e9f6fb;
  --approach-bg:#e9f9f6;
  --teal-blob:#67d7c9;
  --footer-bg:#132f52;
  --field-bg:#1d3e64;
  --bubble:#eff1f4;
  --text:#4f5a66;
  --muted:#8a96a3;
  --white:#ffffff;
}
*{margin:0;padding:0;box-sizing:border-box}
html,body{width:1200px;height:4608px;overflow:hidden}
body{position:relative;background:var(--white);font-family:"Poppins",sans-serif;color:var(--text)}
.abs{position:absolute}
.heading{font-family:"Josefin Sans",sans-serif;font-weight:700;color:var(--navy);letter-spacing:1px;text-transform:uppercase}
.btn{position:absolute;background:var(--accent);color:var(--white);font-family:"Poppins",sans-serif;font-weight:600;font-size:12px;letter-spacing:.5px;text-transform:uppercase;display:flex;align-items:center;justify-content:center;gap:12px}

/* header + hero */
.hero{position:absolute;left:0;top:0;width:1200px;height:737px;background:var(--hero-bg)}
.logo{left:88px;top:31px;font-family:"Poppins",sans-serif;font-weight:600;font-size:21px;letter-spacing:.5px;color:var(--navy)}
.logo span{color:var(--accent-mid)}
.nav{top:36px;font-size:13px;color:var(--navy);text-transform:uppercase;letter-spacing:.3px}
.hero-kicker{left:0;width:1200px;top:212px;text-align:center;font-size:26px;color:var(--accent-mid);font-weight:400}
.hero-title{left:0;width:1200px;top:256px;text-align:center;font-size:64px;line-height:64px}
.stat-value{font-family:"Josefin Sans",sans-serif;font-weight:700;font-size:31px;color:var(--navy);top:555px}
.stat-label{font-size:10px;color:var(--muted);text-transform:uppercase;top:595px;letter-spacing:.3px}

/* expertise */
.section-title{left:0;width:1200px;text-align:center;font-size:44px}
.exp-title{font-size:11.5px;font-weight:600;color:var(--navy);text-transform:uppercase;line-height:15px}
.exp-text{font-size:13px;line-height:19.5px;width:200px}

/* story */
.story-bg{left:308px;top:1375px;width:892px;height:565px;background:var(--story-bg)}
.photo{position:absolute;border-radius:50%;box-shadow:0 30px 50px rgba(12,43,75,.18)}
.body-text{font-size:13.4px;line-height:20.5px}

/* portfolio */
.bubble{position:absolute;border-radius:50%;background:var(--bubble);display:flex;align-items:center;justify-content:center;font-family:"Poppins",sans-serif;font-weight:600;color:#4a5563}

/* approach */
.approach-bg{left:0;top:2614px;width:894px;height:617px;background:var(--approach-bg)}

/* blog */
.card{position:absolute;background:var(--white);box-shadow:0 25px 45px rgba(12,43,75,.10)}
.card-img{position:absolute;left:0;top:0;width:100%}
.card-date{font-size:11px;color:var(--accent-mid)}
.card-title{font-size:15px;font-weight:500;color:var(--navy);line-height:22px}
.card-text{font-size:12.5px;line-height:18px;color:var(--text)}
.card-more{font-size:11.5px;font-weight:600;color:var(--accent);text-transform:uppercase}

/* contact */
.contact{left:0;top:3996px;width:1200px;height:612px;background:var(--footer-bg)}
.field{position:absolute;background:var(--field-bg);font-size:11.5px;color:#c4cfdb;padding:12px 16px}
.copyright{left:0;width:1200px;top:4566px;text-align:center;font-size:11px;color:var(--white);letter-spacing:.3px}
</style>
</head>
<body>

<section class="hero" aria-label="Hero">
  <div class="abs logo">HOLVENCREST <span>VENTURES</span></div>
  <svg class="abs" style="left:588px;top:36px" width="14" height="14" viewBox="0 0 14 14" aria-hidden="true"><path d="M7 1 L13 7 H11 V13 H8.5 V9 H5.5 V13 H3 V7 H1 Z" fill="#0054aa"/></svg>
  <div class="abs nav" style="left:624px">Expertise</div>
  <div class="abs nav" style="left:720px">Story</div>
  <div class="abs nav" style="left:794px">Clients</div>
  <div class="abs nav" style="left:876px">Approach</div>
  <div class="abs nav" style="left:980px">Blog</div>
  <div class="abs nav" style="left:1046px">Contact</div>

  <div class="abs hero-kicker">Finance and Private Equity</div>
  <h1 class="abs heading hero-title">Built by founders<br>for founders</h1>
  <div class="btn" style="left:515px;top:404px;width:170px;height:44px">Find out more</div>

  <div class="abs stat-value" style="left:268px">$40M+</div>
  <div class="abs stat-label" style="left:268px">Money raised</div>
  <div class="abs stat-value" style="left:458px">$125M+</div>
  <div class="abs stat-label" style="left:458px">Attributed revenue</div>
  <div class="abs stat-value" style="left:669px">11</div>
  <div class="abs stat-label" style="left:669px">Company exits</div>
  <div class="abs stat-value" style="left:849px">2</div>
  <div class="abs stat-label" style="left:849px">Awards won</div>
</section>

<h2 class="abs heading section-title" style="top:870px">Area of expertise</h2>

<svg class="abs" style="left:143px;top:978px" width="48" height="48" viewBox="0 0 48 48" fill="none" stroke="#0c2b4b" stroke-width="1.6" aria-hidden="true"><rect x="4" y="4" width="20" height="14" rx="1"/><rect x="24" y="26" width="20" height="14" rx="1"/><path d="M14 18v6M34 40v4M10 44h8M14 24h10v2"/><circle cx="10" cy="34" r="3" stroke="#0677ba"/></svg>
<div class="abs exp-title" style="left:211px;top:982px">Network<br>support</div>
<div class="abs exp-text" style="left:211px;top:1019px">Help you build your network, introducing you to the right people in the right places.</div>

<svg class="abs" style="left:465px;top:975px" width="50" height="50" viewBox="0 0 50 50" fill="none" stroke="#0c2b4b" stroke-width="1.6" aria-hidden="true"><rect x="6" y="14" width="38" height="26" rx="1"/><path d="M6 34h38M20 40v6M30 40v6M16 46h18"/><circle cx="18" cy="8" r="5" stroke="#0677ba"/><path d="M14 26h22M14 22h14"/></svg>
<div class="abs exp-title" style="left:533px;top:982px">Consult on<br>marketing</div>
<div class="abs exp-text" style="left:533px;top:1019px;width:195px">Consult on marketing process, strategies and implementation across your startup.</div>

<svg class="abs" style="left:792px;top:975px" width="50" height="50" viewBox="0 0 50 50" fill="none" stroke="#0c2b4b" stroke-width="1.6" aria-hidden="true"><path d="M8 44V18M4 22l4-6 4 6M42 44V18M38 22l4-6 4 6M25 14V4M21 8l4-4 4 4"/><circle cx="25" cy="30" r="10" stroke="#0677ba"/><path d="M25 24v12M22 27h5a2 2 0 010 4h-4a2 2 0 000 4h5"/></svg>
<div class="abs exp-title" style="left:856px;top:982px">Raising<br>capital</div>
<div class="abs exp-text" style="left:856px;top:1019px;width:190px">Reach out to our extensive connections to raise vital capital for your startup.</div>

<svg class="abs" style="left:143px;top:1139px" width="50" height="50" viewBox="0 0 50 50" fill="none" stroke="#0c2b4b" stroke-width="1.6" aria-hidden="true"><circle cx="25" cy="25" r="22" stroke-dasharray="3 3"/><path d="M10 24l8-6 7 4 7-4 8 6M16 28l6 5 4-2 4 3 6-6"/><path d="M18 18l-4 10" stroke="#0677ba"/></svg>
<div class="abs exp-title" style="left:211px;top:1144px">Mergers &amp;<br>acquisitions</div>
<div class="abs exp-text" style="left:211px;top:1180px;width:180px">Facilitate a smooth mergers and acquisition process for the expansion of your business.</div>

<svg class="abs" style="left:465px;top:1136px" width="52" height="52" viewBox="0 0 52 52" fill="none" stroke="#0c2b4b" stroke-width="1.6" aria-hidden="true"><circle cx="12" cy="40" r="7"/><circle cx="26" cy="36" r="7"/><circle cx="40" cy="32" r="7"/><path d="M6 22l12-8 8 4 16-12" stroke="#0677ba"/><path d="M36 6h6v6" stroke="#0677ba"/></svg>
<div class="abs exp-title" style="left:533px;top:1144px">Revenue<br>acceleration</div>
<div class="abs exp-text" style="left:533px;top:1180px;width:195px">Analyze your revenue streams, providing solutions for kickstarting your revenue.</div>

<svg class="abs" style="left:792px;top:1139px" width="50" height="50" viewBox="0 0 50 50" fill="none" stroke="#0c2b4b" stroke-width="1.6" aria-hidden="true"><rect x="10" y="6" width="34" height="26" rx="1"/><path d="M22 32v8M32 32v8M18 40h18"/><circle cx="10" cy="14" r="6" stroke="#0677ba"/><path d="M16 24h22M20 18h18"/><rect x="6" y="36" width="8" height="8"/></svg>
<div class="abs exp-title" style="left:856px;top:1144px">Integration &amp;<br>incubation</div>
<div class="abs exp-text" style="left:856px;top:1180px;width:190px">Providing training and guidance for startups looking to make their mark on the world.</div>

<div class="abs story-bg" aria-hidden="true"></div>
<svg class="abs" style="left:110px;top:1400px" width="460" height="470" viewBox="0 0 460 470" aria-hidden="true">
  <path d="M70 20 C120 -10 170 20 160 80 L40 200 C20 140 20 60 70 20 Z" fill="#7badd7"/>
  <path d="M380 330 C440 330 460 400 420 440 C390 465 340 470 300 465 Z" fill="#7badd7"/>
</svg>
<div class="photo" role="img" aria-label="Portrait of the firm's founder in a denim shirt, arms crossed" style="left:89px;top:1412px;width:476px;height:476px;background:radial-gradient(circle at 50% 40%,#7a8a93,#4b5a63 70%)"></div>

<h2 class="abs heading" style="left:617px;top:1488px;font-size:44px">Our story</h2>
<p class="abs body-text" style="left:618px;top:1545px;width:490px">Holvencrest Ventures is a venture capital studio firm based in Austin TX with a laser focus on raising solid capital for startups and helping businesses jumpstart their revenue.</p>
<p class="abs body-text" style="left:618px;top:1617px;width:495px">Founded in 2020 by investment expert Marcus Hollenby, Holvencrest Ventures combines proven experience in the venture capital field with a data-driven business analysis strategy to secure capital and reinforce revenue streams for startups and established businesses. Born from the idea that the best way to help founders thrive is to understand their strengths, their weaknesses, their ambitions and their needs – our specialists have been through the entire startup process themselves, and that experience forms our unique approach to business support.</p>
<div class="btn" style="left:619px;top:1799px;width:207px;height:43px">Let's work together</div>

<h2 class="abs heading section-title" style="top:2073px">Our portfolio</h2>
<div class="bubble" style="left:88px;top:2159px;width:110px;height:110px;font-size:15px">Qarvo</div>
<div class="bubble" style="left:319px;top:2166px;width:146px;height:146px;font-size:24px;font-weight:500">lumen</div>
<div class="bubble" style="left:133px;top:2255px;width:196px;height:196px;font-size:26px">Orbitly</div>
<div class="bubble" style="left:345px;top:2327px;width:146px;height:146px;font-size:14px">GenoPath</div>
<div class="bubble" style="left:481px;top:2190px;width:222px;height:222px;font-size:28px;font-weight:400">fernstead</div>
<div class="bubble" style="left:710px;top:2158px;width:140px;height:140px;font-size:15px">urbanloom</div>
<div class="bubble" style="left:688px;top:2328px;width:168px;height:168px;font-size:19px">Kinetra Labs</div>
<div class="bubble" style="left:842px;top:2237px;width:146px;height:146px;font-size:15px">Travexa</div>
<div class="bubble" style="left:989px;top:2173px;width:110px;height:110px;font-size:16px">nextgrain</div>
<div class="bubble" style="left:955px;top:2371px;width:110px;height:110px;font-size:11px;letter-spacing:1px">TERRA LANES</div>

<div class="abs approach-bg" aria-hidden="true"></div>
<svg class="abs" style="left:630px;top:2630px" width="500" height="540" viewBox="0 0 500 540" aria-hidden="true">
  <path d="M300 10 C360 -10 420 30 440 100 C460 170 430 200 400 210 L300 60 Z" fill="#67d7c9"/>
  <path d="M20 400 C0 450 40 500 110 500 C170 500 200 480 210 470 L60 380 Z" fill="#67d7c9"/>
</svg>
<div class="photo" role="img" aria-label="Portrait of a smiling young team member in a blue t-shirt" style="left:634px;top:2676px;width:476px;height:476px;background:radial-gradient(circle at 50% 40%,#a9cfe0,#7fb3cb 70%)"></div>

<h2 class="abs heading" style="left:86px;top:2738px;font-size:44px">Our approach</h2>
<p class="abs body-text" style="left:89px;top:2800px;width:500px">We've built our approach to helping your startup thrive based around three key developmental pillars that guarantee results for our partners.</p>
<p class="abs body-text" style="left:89px;top:2860px;width:505px">First pillar is expertise. We've built our firm on a bank of insights, knowledge and proficiencies honed over years of working with the biggest names in venture capitalism – that experience forms the backbone of every project, every pitch and every investment.</p>
<p class="abs body-text" style="left:89px;top:2960px;width:505px">Second pillar is collaboration. We believe that the best partnerships start with a combined and cooperative approach that benefits all parties every step of the way. We'll always keep our partners up-to-date with our work using regular touchpoints and reports.</p>
<p class="abs body-text" style="left:89px;top:3059px;width:505px">Third and final pillar is trust. We know that our clients and our partners know their industry better than we do, so we trust their input and their ideas – pairing them up with our own business intelligence to guarantee success.</p>

<h2 class="abs heading section-title" style="top:3355px">Latest blog</h2>

<article class="card" style="left:86px;top:3442px;width:431px;height:416px">
  <div class="card-img" role="img" aria-label="Photo of a grey-haired businessman in a white t-shirt, arms crossed" style="height:416px;background:linear-gradient(90deg,#ececec 0%,#d7d7d7 60%,#bdbdbd 100%)"></div>
  <div class="abs card-date" style="left:45px;top:186px;font-size:14px">July 04, 2022</div>
  <div class="abs card-title" style="left:45px;top:210px;font-size:22px;line-height:27px">Some blog heading<br>goes here with ..</div>
  <div class="abs card-more" style="left:45px;top:266px;font-size:13px">Read more</div>
</article>

<article class="card" style="left:535px;top:3442px;width:277px;height:416px">
  <div class="card-img" role="img" aria-label="Photo of a smiling man in a white t-shirt giving a thumbs up" style="height:234px;background:linear-gradient(180deg,#8ec5e6,#6aaedb)"></div>
  <div class="abs card-date" style="left:24px;top:262px">July 04, 2022</div>
  <div class="abs card-title" style="left:24px;top:284px">Some blog heading goes<br>here with des...</div>
  <div class="abs card-text" style="left:24px;top:332px;width:230px">Aenean sollicitudin lorem quis bibendum auctor nisi elit...</div>
  <div class="abs card-more" style="left:24px;top:378px">Read more</div>
</article>

<article class="card" style="left:831px;top:3442px;width:278px;height:416px">
  <div class="card-img" role="img" aria-label="Photo of a man in glasses and a navy shirt" style="height:234px;background:linear-gradient(180deg,#e4e4e4,#cfcfcf)"></div>
  <div class="abs card-date" style="left:24px;top:262px">July 04, 2022</div>
  <div class="abs card-title" style="left:24px;top:284px">Some blog heading goes<br>here with des...</div>
  <div class="abs card-text" style="left:24px;top:332px;width:230px">Aenean sollicitudin lorem quis bibendum auctor nisi elit...</div>
  <div class="abs card-more" style="left:24px;top:378px">Read more</div>
</article>

<section class="abs contact" aria-label="Build with us"></section>
<h2 class="abs heading section-title" style="top:4128px;color:var(--white)">Build with us</h2>
<div class="field" style="left:368px;top:4193px;width:226px;height:38px">Enter your name</div>
<div class="field" style="left:604px;top:4193px;width:226px;height:38px">Enter your email</div>
<div class="field" style="left:368px;top:4239px;width:462px;height:38px">Enter phone number</div>
<div class="field" style="left:368px;top:4288px;width:462px;height:116px">Type your text...</div>
<div class="btn" style="left:508px;top:4418px;width:182px;height:39px;background:var(--accent-mid)">Submit now
  <svg width="13" height="13" viewBox="0 0 14 14" aria-hidden="true"><path d="M1 6.5 L13 1 L8 13 L6.5 8 Z" fill="#ffffff"/></svg>
</div>
<div class="abs" style="left:88px;top:4549px;width:1024px;height:1px;background:#2e4c70"></div>
<div class="abs copyright">COPYRIGHT © 2022 HOLVENCREST.COM</div>
<div class="abs" style="left:1135px;top:4530px;width:40px;height:40px;border-radius:50%;background:var(--white);display:flex;align-items:center;justify-content:center">
  <svg width="10" height="8" viewBox="0 0 10 8" aria-hidden="true"><path d="M1 6 L5 2 L9 6" stroke="#0c2b4b" stroke-width="1.6" fill="none"/></svg>
</div>

</body>
</html>
```